Healthcare Consulting company business card

We are looking for a business card design for a new healthcare consulting company. The company is looking to provide assistance to large healthcare organisations in the following categories:
Acute care and critical care
Tender documents and applications
CV, job applications and interview skills
scientific lecture presentation preparations and skills
research and quality activities
medical equipment and device consulting
hemofiltration liaising.
Please see the attached file below for the design brief.
Alternative designs are welcomed.
Business
Contact Information for Business Card
Name: Rex Tulloch
Mobile: 0427 816 094
Email: rextullochconsulting@mailbox-example.com
Website: www.rextullochconsulting-example.com.au

```html
<!DOCTYPE html>
<html lang="en">
<head>
<meta charset="utf-8">
<title>Rex Tulloch Consulting – Business Card</title>
<link href="https://fonts.googleapis.com/css2?family=Arimo:ital,wght@0,400;0,700;1,700&display=swap" rel="stylesheet">
<style>
  :root {
    --brand-blue: #265c9c;
    --paper: #ffffff;
    --card-edge: #2a2a2a;
  }
  html, body {
    margin: 0;
    padding: 0;
    width: 1200px;
    height: 1200px;
    overflow: hidden;
    background: var(--paper);
    font-family: "Arimo", Arial, sans-serif;
  }
  .stage {
    position: relative;
    width: 1200px;
    height: 1200px;
  }
  .card {
    position: absolute;
    left: 180px;
    width: 838px;
    height: 479px;
    box-sizing: border-box;
  }
  .card--front {
    top: 93px;
    background: var(--paper);
    border: 1.5px solid var(--card-edge);
    color: var(--brand-blue);
  }
  .card--back {
    top: 626px;
    background: var(--brand-blue);
    color: var(--paper);
  }
  .holder {
    position: absolute;
    left: 61px;
    top: 88px;
    margin: 0;
  }
  .holder__name {
    font-size: 35px;
    font-weight: 700;
    line-height: 1;
    margin: 0;
  }
  .holder__credentials {
    font-size: 22px;
    font-style: italic;
    font-weight: 700;
  }
  .holder__role {
    font-size: 25px;
    margin: 6px 0 0;
    line-height: 1;
  }
  .contacts {
    position: absolute;
    left: 56px;
    top: 188px;
    margin: 0;
    padding: 0;
    list-style: none;
  }
  .contacts__item {
    display: flex;
    align-items: center;
    height: 40px;
    font-size: 25px;
  }
  .contacts__icon {
    width: 24px;
    height: 24px;
    margin-right: 18px;
    flex: none;
  }
  .wordmark {
    position: absolute;
    text-align: center;
    font-weight: 700;
    line-height: 1;
  }
  .card--front .wordmark {
    left: 540px;
    top: 84px;
    width: 250px;
  }
  .card--front .wordmark__name { font-size: 27px; }
  .card--front .wordmark__tag { font-size: 14px; letter-spacing: 9px; margin-top: 10px; }
  .card--back .wordmark {
    left: 219px;
    top: 140px;
    width: 400px;
  }
  .card--back .wordmark__name { font-size: 42px; }
  .card--back .wordmark__tag { font-size: 20px; letter-spacing: 14px; margin-top: 14px; }
  .services {
    position: absolute;
    left: 57px;
    top: 352px;
    display: flex;
    gap: 70px;
  }
  .card--back .services { top: 340px; }
  .services__tile {
    width: 89px;
    height: 89px;
    border-radius: 5px;
  }
  .card--front .services__tile { background: var(--brand-blue); }
  .card--back .services__tile { background: var(--paper); }
</style>
</head>
<body>
<main class="stage">

  <section class="card card--front" aria-label="Card front">
    <div class="holder">
      <h1 class="holder__name">Dr. Rex Tulloch <span class="holder__credentials">R.N. PhD.</span></h1>
      <p class="holder__role">Director</p>
    </div>

    <div class="wordmark">
      <div class="wordmark__name">REX TULLOCH</div>
      <div class="wordmark__tag">CONSULTING</div>
    </div>

    <ul class="contacts">
      <li class="contacts__item">
        <svg class="contacts__icon" viewBox="0 0 24 24" aria-hidden="true">
          <rect x="6" y="2" width="12" height="20" rx="3" fill="none" stroke="currentColor" stroke-width="2.4"/>
          <circle cx="12" cy="18" r="1.4" fill="currentColor"/>
        </svg>
        0427 816 094
      </li>
      <li class="contacts__item">
        <svg class="contacts__icon" viewBox="0 0 24 24" aria-hidden="true">
          <rect x="1" y="6" width="22" height="13" fill="currentColor"/>
          <path d="M1 6 L12 14 L23 6 M1 19 L9 12 M23 19 L15 12" fill="none" stroke="#fff" stroke-width="1.3"/>
        </svg>
        rextullochconsulting@mailbox-example.com
      </li>
      <li class="contacts__item">
        <svg class="contacts__icon" viewBox="0 0 24 24" aria-hidden="true">
          <g fill="none" stroke="currentColor" stroke-width="2">
            <circle cx="12" cy="12" r="10"/>
            <ellipse cx="12" cy="12" rx="4.5" ry="10"/>
            <path d="M2 12 H22 M4 7 H20 M4 17 H20"/>
          </g>
        </svg>
        www.rextullochconsulting-example.com.au
      </li>
    </ul>

    <div class="services">
      <div class="services__tile" role="img" aria-label="Pictogram: tender and funding applications"></div>
      <div class="services__tile" role="img" aria-label="Pictogram: heart with heartbeat line, acute and critical care"></div>
      <div class="services__tile" role="img" aria-label="Pictogram: hospital bed with monitor, medical equipment"></div>
      <div class="services__tile" role="img" aria-label="Pictogram: figures under an arc, career and interview skills"></div>
      <div class="services__tile" role="img" aria-label="Pictogram: test tubes and microscope, research and quality"></div>
    </div>
  </section>

  <section class="card card--back" aria-label="Card back">
    <div class="wordmark">
      <div class="wordmark__name">REX TULLOCH</div>
      <div class="wordmark__tag">CONSULTING</div>
    </div>

    <div class="services">
      <div class="services__tile" role="img" aria-label="Pictogram: tender and funding applications"></div>
      <div class="services__tile" role="img" aria-label="Pictogram: heart with heartbeat line, acute and critical care"></div>
      <div class="services__tile" role="img" aria-label="Pictogram: hospital bed with monitor, medical equipment"></div>
      <div class="services__tile" role="img" aria-label="Pictogram: figures under an arc, career and interview skills"></div>
      <div class="services__tile" role="img" aria-label="Pictogram: test tubes and microscope, research and quality"></div>
    </div>
  </section>

</main>
</body>
</html>
```